Business Card and Letterhead Design Using Our New Logo
Copper Wren Stud
Bright & Fun-filled
Marwen Adkiss
PO Box 487
BRAMBLEDOWN WA 6217
marwen@copperwrenstud.com.au
ABN 52 318 604 917 (on letterhead only)
Copper Wren Stud is a family run business producing Elite Sport Ponies and Horses. We also manufacture custom made show accessories and provide show preparation services.
Our stationery should create a sense of beauty, elegance and sophistication.
For our letter head we'd like the logo in colour to be in the top left hand corner of the page. The PO Box etc to be in the top right corner. And in the bottom right corner a watermark of the logo that bleeds over the edge of the paper.
For the business card we'd like one side to be just the logo either colour or black & grey / white & grey. On the side with the details we'd like the logo in colour.
All details text to be Quciksand Book as appears in the logo also prefer this to be grey rather than black.
Dummy version of letterhead idea just need to add watermark horses black and grey to bottom righthand side.
vector logo file

```html
<!DOCTYPE html>
<html lang="en">
<head>
<meta charset="utf-8">
<title>Copper Wren Stud – Stationery</title>
<link rel="stylesheet" href="https://fonts.googleapis.com/css2?family=Quicksand:wght@400;500;600&display=swap">
<style>
  :root {
    --backdrop: #ece6dc;
    --paper: #ffffff;
    --ink-grey: #6f6f6f;
    --ink-soft: #9a9a9a;
    --brand-red: #a3174a;
    --brand-olive: #7a8348;
    --watermark: #ececec;
    --label: #5a4a3a;
  }
  * { box-sizing: border-box; margin: 0; padding: 0; }
  html, body { width: 1200px; height: 1080px; overflow: hidden; }
  body {
    background: var(--backdrop);
    font-family: "Quicksand", sans-serif;
    color: var(--ink-grey);
    position: relative;
  }
  .brand-name {
    font-family: "Quicksand", sans-serif;
    font-weight: 600;
    color: var(--brand-red);
    white-space: nowrap;
  }

  /* Business card front */
  .card { position: absolute; background: var(--paper); border-radius: 12px; overflow: hidden;
          box-shadow: 0 2px 6px rgba(0,0,0,.18); }
  .card-front { left: 41px; top: 331px; width: 296px; height: 188px; }
  .card-front .swoosh { position: absolute; inset: 0; }
  .card-front .brand-name { position: absolute; left: 16px; top: 30px; width: 110px;
                            font-size: 18px; line-height: 21px; white-space: normal; }
  .card-front .holder { position: absolute; left: 132px; top: 52px; font-size: 10px; color: var(--ink-grey); white-space: nowrap; }
  .card-front .details { position: absolute; left: 16px; top: 122px; font-size: 7px; line-height: 10px; color: var(--ink-soft); white-space: nowrap; }

  /* Business card back */
  .card-back { left: 41px; top: 550px; width: 296px; height: 176px; }
  .card-back .brand-name { position: absolute; left: 0; right: 0; top: 62px; text-align: center;
                           font-size: 20px; color: var(--ink-grey); }
  .card-back .web { position: absolute; left: 0; right: 0; top: 122px; text-align: center;
                    font-size: 10px; letter-spacing: 1px; color: var(--ink-grey); font-weight: 500; }

  .card-label { position: absolute; left: 41px; width: 296px; text-align: center;
                font-size: 12px; font-variant: small-caps; letter-spacing: 1.5px; color: var(--label); font-weight: 600; }
  .label-front { top: 533px; }
  .label-back { top: 738px; }

  /* Letterhead */
  .letterhead { position: absolute; left: 401px; top: 9px; width: 771px; height: 1060px;
                background: var(--paper); overflow: hidden; box-shadow: 0 2px 8px rgba(0,0,0,.15); }
  .letterhead .brand-name { position: absolute; left: 40px; top: 100px; font-size: 30px; }
  .letterhead .contact { position: absolute; left: 560px; top: 46px; font-size: 9px; line-height: 12px;
                         color: var(--ink-soft); text-transform: uppercase; white-space: nowrap; }
  .letterhead .contact p + p { margin-top: 12px; }
  .letterhead .contact .email { text-transform: none; }
  .letterhead .watermark { position: absolute; left: 220px; top: 670px; width: 620px; height: 360px;
                           border-radius: 50% 40% 30% 50%;
                           background: radial-gradient(ellipse at 45% 50%, var(--watermark) 0%, #f6f6f6 60%, rgba(255,255,255,0) 75%); }
</style>
</head>
<body>

  <section class="card card-front">
    <svg class="swoosh" width="296" height="188" viewBox="0 0 296 188" aria-hidden="true">
      <path d="M296 0 L236 0 C250 60 200 140 110 188 L296 188 Z" fill="var(--brand-olive)"/>
      <path d="M226 0 L236 0 C250 60 200 140 110 188 L96 188 C185 140 238 62 226 0 Z" fill="var(--brand-red)"/>
    </svg>
    <span class="brand-name">Copper Wren Stud</span>
    <span class="holder">Marwen Adkiss</span>
    <div class="details">
      <p>PO Box 487 Brambledown WA 6217</p>
      <p>M 0412 386 045</p>
      <p>F 9571 2284</p>
      <p>E marwen@copperwrenstud.com.au</p>
    </div>
  </section>
  <p class="card-label label-front">Business Card Front</p>

  <section class="card card-back">
    <span class="brand-name">Copper Wren Stud</span>
    <span class="web">www.copperwrenstud.com.au</span>
  </section>
  <p class="card-label label-back">Business Card Back</p>

  <section class="letterhead">
    <span class="brand-name">Copper Wren Stud</span>
    <div class="contact">
      <p>PO Box 487<br>Brambledown WA 6217</p>
      <p>Mobile 0412 386 045<br>Fax 9571 2284</p>
      <p class="email">marwen@copperwrenstud.com.au</p>
      <p>ABN 52 318 604 917</p>
    </div>
    <div class="watermark" role="img" aria-label="Faint grey line drawing of a galloping horse as a watermark, bleeding off the right edge"></div>
  </section>

</body>
</html>
```